KV Taxidermy

I need business Cards with my logo and a background photo of one of my taxidermy mounts.
I would like a black back drop behind it all and what ever looks best for my contact information (red or white?)
Marcus Pellow
555-218-4907
kvtaxidermy512@mailvex.net
Chatterly page

```html
<!DOCTYPE html>
<html lang="en">
<head>
<meta charset="utf-8">
<title>KV Taxidermy — Business Card</title>
<link href="https://fonts.googleapis.com/css2?family=Bebas+Neue&display=swap" rel="stylesheet">
<style>
  :root {
    --stage: #6e6e6e;
    --card: #1b1b1b;
    --red: #e3211f;
    --white: #ffffff;
    --silver: #c4c6c8;
    --fleece: #e9e7e2;
    --horn: #8a5f3c;
  }
  * { margin: 0; padding: 0; box-sizing: border-box; }
  html, body {
    width: 1200px; height: 884px; overflow: hidden;
    background: var(--stage);
  }
  .canvas {
    width: 1200px; height: 884px;
    display: flex; align-items: center; justify-content: center;
  }
  .card {
    position: relative;
    width: 1080px; height: 617px;
    background: var(--card);
    font-family: "Bebas Neue", "Oswald", sans-serif;
    overflow: hidden;
  }
  .mount-photo {
    position: absolute;
    left: 130px; top: 40px;
    width: 400px; height: 520px;
    background: linear-gradient(180deg, var(--horn) 0%, #b59a82 35%, var(--fleece) 70%, var(--fleece) 100%);
  }
  .info {
    position: absolute;
    left: 560px; top: 0;
    width: 440px; height: 100%;
    display: flex; flex-direction: column; align-items: center;
  }
  .brand {
    margin-top: 140px;
    display: flex; align-items: center; gap: 14px;
    color: var(--silver);
    font-size: 46px; letter-spacing: 4px;
  }
  .brand-mark {
    width: 30px; height: 30px;
    background: var(--silver);
  }
  .owner-name {
    margin-top: 80px;
    color: var(--red);
    font-size: 60px; line-height: 1;
    font-weight: 400;
    letter-spacing: 1px;
  }
  .contact-icons {
    margin-top: 26px;
    display: flex; gap: 22px; align-items: center;
  }
  .contact-icons svg { width: 24px; height: 24px; display: block; }
  .social-square { width: 20px; height: 20px; background: var(--red); border-radius: 3px; }
  .contact-list {
    margin-top: 10px;
    list-style: none;
    text-align: center;
    color: var(--white);
    font-size: 38px; line-height: 1.02;
    letter-spacing: 0.5px;
  }
</style>
</head>
<body>
  <main class="canvas">
    <section class="card">
      <div class="mount-photo" role="img" aria-label="Photo of a white Dall sheep ram taxidermy mount with curled brown horns"></div>

      <div class="info">
        <div class="brand">
          <span class="brand-mark"></span>
          <span class="brand-name">KV Taxidermy</span>
        </div>

        <h1 class="owner-name">Marcus Pellow</h1>

        <div class="contact-icons">
          <svg viewBox="0 0 24 24" aria-hidden="true">
            <path fill="var(--red)" d="M6.6 10.8c1.4 2.8 3.8 5.1 6.6 6.6l2.2-2.2c.3-.3.7-.4 1-.2 1.1.4 2.3.6 3.6.6.6 0 1 .4 1 1V20c0 .6-.4 1-1 1C10.6 21 3 13.4 3 4c0-.6.4-1 1-1h3.5c.6 0 1 .4 1 1 0 1.3.2 2.5.6 3.6.1.3 0 .7-.2 1L6.6 10.8z"/>
          </svg>
          <svg viewBox="0 0 24 24" aria-hidden="true">
            <rect x="2.5" y="5" width="19" height="14" fill="none" stroke="var(--red)" stroke-width="2"/>
            <path d="M3 6l9 7 9-7" fill="none" stroke="var(--red)" stroke-width="2"/>
          </svg>
          <span class="social-square" aria-label="Chatterly"></span>
        </div>

        <ul class="contact-list">
          <li>555-218-4907</li>
          <li>kvtaxidermy512@mailvex.net</li>
          <li>/KVTaxiDermy</li>
        </ul>
      </div>
    </section>
  </main>
</body>
</html>
```